Business card design for modern law firm

We need new business cards. Information about our law firm can be found at www.qrtl-recht.de. The business cards should include the information that we have offices in Berlin and Stuttgart. They should be customizable for all attorneys who are partially located in Berlin and partially in Stuttgart. Example of the information:
Jonas Ackermann
lawyer
Specialist lawyer for copyright and media law
Lindenweg 17, 70374 Stuttgart
ackermann@qrtl-recht.de
+49 711 483 15 260
www.qrtl-recht.de
It is important for us that we can edit the cards independently, i.e. exchange names and contact details.
In addition, a QR code for a VCard should be placed on the card.
The design of the old maps is attached; the new design should clearly distinguish itself from them. They should be more modern. The design is ideally based on the design of the website www.qrtl-recht.de.
Industry/Entity Type
Rechtsanwalt
Contact Information for Business Card
Siehe projektbeschreibung

```html
<!DOCTYPE html>
<html lang="de">
<head>
<meta charset="utf-8">
<title>QRTL Rechtsanwälte – Visitenkarte</title>
<link rel="stylesheet" href="https://fonts.googleapis.com/css2?family=Poppins:wght@400;500;800&family=Roboto+Slab:wght@700&display=swap">
<style>
  :root {
    --stage: #141416;
    --card: #242426;
    --green: #9fcd2b;
    --white: #f2f2f2;
    --muted: #d0d0d0;
    --code-bg: #f2f2f2;
  }
  * { margin: 0; padding: 0; box-sizing: border-box; }
  html, body { width: 1200px; height: 952px; overflow: hidden; background: var(--stage); }
  .stage {
    width: 1200px; height: 952px;
    display: flex; flex-direction: column; align-items: center; justify-content: center; gap: 48px;
  }
  .card {
    position: relative;
    width: 660px; height: 400px;
    background: var(--card);
    box-shadow: 0 18px 40px rgba(0,0,0,.55);
    font-family: "Poppins", sans-serif;
    color: var(--white);
    overflow: hidden;
  }
  /* front */
  .front-wordmark {
    position: absolute; left: 86px; top: 78px;
    font-family: "Poppins", sans-serif; font-weight: 500;
    font-size: 150px; line-height: 1; letter-spacing: -2px;
    color: var(--green);
  }
  .front-tagline { position: absolute; left: 312px; top: 272px; }
  .tagline-main {
    font-family: "Roboto Slab", serif; font-weight: 700;
    color: var(--green); font-size: 25px; letter-spacing: 4.5px; text-transform: uppercase;
  }
  .tagline-sub {
    font-family: "Roboto Slab", serif; font-weight: 700;
    color: var(--white); font-size: 17px; letter-spacing: 3px; margin-top: 2px;
  }
  .tagline-sub .legal-form { text-transform: none; letter-spacing: 1px; font-size: 14px; }
  /* back */
  .back-brand { position: absolute; left: 48px; top: 84px; }
  .back-wordmark {
    font-weight: 500; font-size: 46px; line-height: 1; color: var(--green); letter-spacing: -1px;
  }
  .back-brand .tagline-main { font-size: 13px; letter-spacing: 2.4px; margin-top: 8px; }
  .back-brand .tagline-sub { font-size: 9.5px; letter-spacing: 1.6px; margin-top: 1px; }
  .back-brand .legal-form { font-size: 8px; }
  .offices { position: absolute; left: 48px; top: 236px; list-style: none; }
  .office { margin-bottom: 12px; }
  .office-city {
    font-size: 10px; font-weight: 500; letter-spacing: 1.5px; text-transform: uppercase;
    color: var(--green); line-height: 1.4;
  }
  .office-address { font-size: 13px; color: var(--muted); line-height: 1.3; }
  .divider { position: absolute; left: 290px; top: 60px; width: 2px; height: 280px; }
  .contact { position: absolute; left: 322px; top: 66px; }
  .person-name {
    font-weight: 800; font-size: 24px; letter-spacing: 1px; text-transform: uppercase;
    color: var(--green); line-height: 1.15;
  }
  .person-role { font-size: 15px; color: var(--muted); line-height: 1.3; }
  .person-specialty { font-size: 11.5px; color: var(--muted); line-height: 1.4; margin-bottom: 20px; }
  .contact-list { list-style: none; }
  .contact-list li {
    display: flex; align-items: center; gap: 10px;
    font-size: 14px; color: var(--white); line-height: 1; margin-bottom: 13px;
  }
  .contact-list svg { width: 14px; height: 14px; flex: none; }
  .vcard-code {
    position: absolute; right: 36px; bottom: 36px;
    width: 84px; height: 84px; background: var(--code-bg);
  }
</style>
</head>
<body>
<main class="stage">

  <section class="card card-front" aria-label="Vorderseite">
    <div class="front-wordmark">qrtl</div>
    <div class="front-tagline">
      <div class="tagline-main">Rechtsanwälte</div>
      <div class="tagline-sub">LEGAL SERVICES <span class="legal-form">PartmbB</span></div>
    </div>
  </section>

  <section class="card card-back" aria-label="Rückseite">
    <div class="back-brand">
      <div class="back-wordmark">qrtl</div>
      <div class="tagline-main">Rechtsanwälte</div>
      <div class="tagline-sub">LEGAL SERVICES <span class="legal-form">PartmbB</span></div>
    </div>

    <ul class="offices">
      <li class="office">
        <p class="office-city">Stuttgart</p>
        <p class="office-address">Lindenweg 17, 70374 Stuttgart</p>
      </li>
      <li class="office">
        <p class="office-city">Berlin</p>
        <p class="office-address">Ahornstraße 9, 10787 Berlin</p>
      </li>
    </ul>

    <svg class="divider" viewBox="0 0 2 280" preserveAspectRatio="none" aria-hidden="true">
      <defs>
        <linearGradient id="dividerFade" x1="0" y1="0" x2="0" y2="1">
          <stop offset="0" stop-color="#9fcd2b" stop-opacity="0"/>
          <stop offset=".3" stop-color="#9fcd2b"/>
          <stop offset=".7" stop-color="#9fcd2b"/>
          <stop offset="1" stop-color="#9fcd2b" stop-opacity="0"/>
        </linearGradient>
      </defs>
      <rect width="2" height="280" fill="url(#dividerFade)"/>
    </svg>

    <div class="contact">
      <h1 class="person-name">Jonas Ackermann</h1>
      <p class="person-role">lawyer</p>
      <p class="person-specialty">Specialist lawyer for copyright and media law</p>
      <ul class="contact-list">
        <li>
          <svg viewBox="0 0 24 24" aria-hidden="true"><path fill="#9fcd2b" d="M6.6 10.8a15 15 0 0 0 6.6 6.6l2.2-2.2a1 1 0 0 1 1-.25 11.4 11.4 0 0 0 3.6.57 1 1 0 0 1 1 1V20a1 1 0 0 1-1 1A17 17 0 0 1 3 4a1 1 0 0 1 1-1h3.5a1 1 0 0 1 1 1c0 1.25.2 2.45.57 3.57a1 1 0 0 1-.25 1z"/></svg>
          +49 711 483 15 260
        </li>
        <li>
          <svg viewBox="0 0 24 24" aria-hidden="true"><path fill="#9fcd2b" d="M2 5h20v14H2z"/><path fill="none" stroke="#242426" stroke-width="2" d="M2 6l10 7 10-7"/></svg>
          ackermann@qrtl-recht.de
        </li>
        <li>
          <svg viewBox="0 0 24 24" aria-hidden="true"><circle cx="12" cy="12" r="10" fill="#9fcd2b"/><path fill="none" stroke="#242426" stroke-width="1.6" d="M2 12h20M12 2c3 3 3 17 0 20M12 2c-3 3-3 17 0 20"/></svg>
          www.qrtl-recht.de
        </li>
      </ul>
    </div>

    <div class="vcard-code" role="img" aria-label="QR-Code mit vCard-Kontaktdaten"></div>
  </section>

</main>
</body>
</html>
```